Municipal election sign

I am looking to have a sign and a post card designed for an upcoming election in the MD of Lakeshore Alberta Canada. Having my name (Joel Branwick) on the sign/Post card in big clear letters is important as well as the election date(October 16th) The position, if it matters is counselor in Ward 6. On the post cards I would like have some of my key points from the about section of my fb page(Link bellow) on the back of the card.

https://www.pagelink.example/Joelbranwickward6

```html
<!DOCTYPE html>
<html lang="en">
<head>
<meta charset="utf-8">
<title>Joel Branwick – Ward 6 Election Sign</title>
<link rel="stylesheet" href="https://fonts.googleapis.com/css2?family=Oswald:wght@600;700&family=Open+Sans:wght@600;700;800&display=swap">
<style>
  :root {
    --page-bg: #ecebe8;
    --slate: #4a4a4b;
    --field-green: #5f7f33;
    --gold: #d9a52a;
    --ink: #222222;
    --bar: #2b2b2b;
    --white: #ffffff;
    --yellow: #ffea00;
    --shirt-blue: #6f8fcf;
    --shirt-blue-dark: #4d6aa8;
  }
  * { box-sizing: border-box; margin: 0; padding: 0; }
  html, body { width: 1200px; height: 850px; overflow: hidden; }
  body { background: var(--page-bg); position: relative; font-family: "Open Sans", Arial, sans-serif; }

  .sign {
    position: absolute; left: 87px; top: 167px;
    width: 1028px; height: 516px; overflow: hidden;
    background: var(--field-green);
    box-shadow: 0 6px 18px rgba(0,0,0,0.25);
  }
  .sign-backdrop { position: absolute; inset: 0; width: 100%; height: 100%; }

  .candidate-photo {
    position: absolute; left: 4px; top: 40px;
    width: 400px; height: 476px;
    border-radius: 150px 150px 0 0;
    background: linear-gradient(180deg, #d9a98f 0%, #c99a80 38%, var(--shirt-blue) 58%, var(--shirt-blue-dark) 100%);
  }

  .district-mark {
    position: absolute; left: 676px; top: 9px;
    width: 204px; height: 105px; background: var(--white);
    display: flex; align-items: center; justify-content: center; gap: 8px;
    font-family: "Oswald", Arial, sans-serif; font-weight: 600;
    font-size: 15px; color: var(--ink); text-transform: uppercase; text-align: center;
    line-height: 1.15;
  }
  .district-mark .mark-dot { width: 14px; height: 14px; border-radius: 50%; background: var(--field-green); flex: none; }

  .message { position: absolute; left: 500px; width: 518px; top: 116px; text-align: center; }
  .headline {
    font-family: "Oswald", Arial, sans-serif; font-weight: 700;
    font-size: 59px; line-height: 60px; color: var(--ink); letter-spacing: 0.5px;
  }
  .council { font-weight: 700; font-size: 22px; line-height: 26px; color: var(--white); }
  .ward { font-weight: 800; font-size: 41px; line-height: 46px; color: var(--yellow); }
  .candidate-name {
    font-weight: 800; font-size: 56px; line-height: 62px; color: var(--white);
    letter-spacing: 0.5px; text-transform: uppercase;
  }
  .notice {
    display: block; margin: 4px auto 0; width: 486px; height: 48px;
    background: var(--bar);
    font-family: "Oswald", Arial, sans-serif; font-weight: 700;
    font-size: 34px; line-height: 48px; color: var(--yellow);
  }
  .location { font-weight: 700; font-size: 21px; line-height: 26px; color: var(--white); margin-top: 8px; }
  .election-date { font-weight: 800; font-size: 50px; line-height: 56px; color: var(--white); }
  .election-date .month { color: var(--yellow); }

  .contact-bar {
    position: absolute; left: 400px; right: 0; bottom: 0; height: 58px;
    background: var(--bar); display: flex; align-items: center;
    padding-left: 20px; gap: 16px; color: var(--white);
  }
  .contact-phone { font-weight: 800; font-size: 29px; }
  .contact-email { display: flex; align-items: center; gap: 8px; font-weight: 600; font-size: 19px; }
  .contact-email svg { width: 20px; height: 20px; }
</style>
</head>
<body>
  <div class="sign">
    <svg class="sign-backdrop" viewBox="0 0 1028 516" aria-hidden="true">
      <defs>
        <linearGradient id="goldBand" x1="0" y1="0" x2="1" y2="1">
          <stop offset="0" stop-color="#b8861c"/>
          <stop offset="0.5" stop-color="#f1cf6a"/>
          <stop offset="1" stop-color="#b8861c"/>
        </linearGradient>
      </defs>
      <rect width="1028" height="516" fill="#5f7f33"/>
      <polygon points="560,0 800,0 640,260" fill="#6a8a39" opacity="0.6"/>
      <polygon points="900,0 1028,0 1028,300" fill="#557530" opacity="0.6"/>
      <path d="M0 0 H358 Q555 240 395 516 H0 Z" fill="#4a4a4b"/>
      <polygon points="0,0 220,0 80,260" fill="#434344" opacity="0.7"/>
      <polygon points="150,300 360,120 330,516" fill="#525253" opacity="0.6"/>
      <path d="M358 0 H405 Q600 250 430 516 H395 Q555 240 358 0 Z" fill="url(#goldBand)"/>
    </svg>

    <div class="candidate-photo" role="img" aria-label="Photo of candidate Joel Branwick, smiling, arms crossed, in a blue shirt"></div>

    <div class="district-mark"><span class="mark-dot"></span><span>Lakeshore Rural<br>District</span></div>

    <div class="message">
      <h1 class="headline">Candidate for the</h1>
      <p class="council">MD of Lakeshore Council</p>
      <p class="ward">in Ward 6</p>
      <p class="candidate-name">Joel Branwick</p>
      <p class="notice">Upcoming election in the</p>
      <p class="location">MD of Lakeshore Alberta Canada</p>
      <p class="election-date"><span class="month">October</span> 16th</p>
    </div>

    <div class="contact-bar">
      <span class="contact-phone">Call 780-555-0142</span>
      <span class="contact-email">
        <svg viewBox="0 0 20 20" aria-hidden="true">
          <circle cx="10" cy="10" r="9" fill="none" stroke="#fff" stroke-width="1.5"/>
          <rect x="5" y="6.5" width="10" height="7" fill="#fff"/>
          <path d="M5 6.5 L10 10.5 L15 6.5" fill="none" stroke="#2b2b2b" stroke-width="1"/>
        </svg>
        jbranwick@northfield.example
      </span>
    </div>
  </div>
</body>
</html>
```